Project Manager Business Card for Top Architectural Firm

Update and design a stunning Senior Project Manager Business Card

MARCO T. DRUMMOND II
Senior Project Manager

H A L C Y O N
A R C H I T E C T U R E L L C.
www.HalcyonGrandEstates.example
4127 NW 52nd Ter. Suite 2308
Miami, FL 33148
C: (305) 555-0184
mdrummond.halcyongrandestates@mailbox.example

Looking to have the logo to be UV Spot ink printed and to be prominent.

Target Market(s)

High end real estate architecture construction

Industry/Entity Type

Architect

Contact Information for Business Card

MARCO T. DRUMMOND II
Senior Project Manager

H A L C Y O N
Miami, FL 33148
C: (305) 555-0184

Font styles to use
Sans Serif

Colors

Designer to choose colors to be used in the design.

Requirements
Must have
• Prominent Logo

```html
<!DOCTYPE html>
<html lang="en">
<head>
<meta charset="utf-8">
<title>Halcyon Architecture LLC — Business Card</title>
<link href="https://fonts.googleapis.com/css2?family=Montserrat:wght@300;400;500;600&display=swap" rel="stylesheet">
<style>
  :root {
    --stage: #1f1f1f;
    --card-black: #121212;
    --card-white: #ffffff;
    --ink: #1a1a1a;
    --ink-soft: #3a3a3a;
    --brand-blue: #1a8ccc;
    --brand-blue-dark: #0f74b3;
    --silver: #c9c9c9;
    --silver-dim: #8a8a8a;
  }
  * { box-sizing: border-box; margin: 0; padding: 0; }
  html, body {
    width: 1200px; height: 900px; overflow: hidden;
    background: var(--stage);
    font-family: "Montserrat", sans-serif;
  }
  .stage { position: relative; width: 1200px; height: 900px; }

  .card {
    position: absolute;
    left: 285px;
    width: 630px; height: 360px;
    border-radius: 18px;
    overflow: hidden;
    box-shadow: 0 14px 30px rgba(0,0,0,.45);
  }

  /* Back side */
  .card--back { top: 60px; background: var(--card-black); }
  .wordmark {
    position: absolute;
    display: flex; align-items: center; gap: 18px;
  }
  .wordmark__dot {
    width: 44px; height: 44px; border-radius: 50%;
    flex: none;
  }
  .wordmark__text {
    font-weight: 300;
    line-height: 1.25;
  }
  .wordmark__name { display: block; font-size: 46px; letter-spacing: 14px; }
  .wordmark__sub  { display: block; font-size: 13px; letter-spacing: 6px; }

  .card--back .wordmark { left: 140px; top: 118px; }
  .card--back .wordmark__dot { background: var(--silver); }
  .card--back .wordmark__text { color: var(--silver); }
  .back__url {
    position: absolute; left: 0; right: 0; top: 258px;
    text-align: center;
    color: var(--silver-dim);
    font-size: 14px; letter-spacing: 3px;
  }

  /* Front side */
  .card--front { top: 480px; background: var(--card-white); }
  .card--front .wordmark { left: 40px; top: 196px; gap: 12px; }
  .card--front .wordmark__dot { width: 30px; height: 30px; background: var(--brand-blue); }
  .card--front .wordmark__text { color: var(--ink); }
  .card--front .wordmark__name { font-size: 30px; letter-spacing: 8px; }
  .card--front .wordmark__sub  { font-size: 8.5px; letter-spacing: 3.6px; }

  .contact {
    position: absolute; right: 36px; top: 36px;
    text-align: right;
    color: var(--ink);
  }
  .contact__name {
    color: var(--brand-blue);
    font-size: 19px; font-weight: 600; letter-spacing: .3px;
  }
  .contact__title { font-size: 12.5px; font-weight: 400; color: var(--ink-soft); margin-top: 2px; }
  .contact__lines { margin-top: 38px; font-size: 12.5px; line-height: 1.7; }

  .company {
    position: absolute; right: 36px; top: 250px;
    text-align: right;
  }
  .company__name {
    color: var(--brand-blue);
    font-size: 18px; font-weight: 500;
    padding-bottom: 3px;
    border-bottom: 1.5px solid var(--brand-blue);
  }
  .company__address { font-size: 11px; color: var(--ink-soft); margin-top: 4px; }

  .card__band {
    position: absolute; left: 0; right: 0; bottom: 0; height: 14px;
    background: linear-gradient(90deg, var(--brand-blue-dark), var(--brand-blue));
  }
</style>
</head>
<body>
<main class="stage">

  <section class="card card--back" aria-label="Card back">
    <div class="wordmark">
      <span class="wordmark__dot"></span>
      <span class="wordmark__text">
        <span class="wordmark__name">HALCYON</span>
        <span class="wordmark__sub">ARCHITECTURE LLC.</span>
      </span>
    </div>
    <p class="back__url">www.HalcyonGrandEstates.example</p>
  </section>

  <section class="card card--front" aria-label="Card front">
    <div class="wordmark">
      <span class="wordmark__dot"></span>
      <span class="wordmark__text">
        <span class="wordmark__name">HALCYON</span>
        <span class="wordmark__sub">ARCHITECTURE LLC.</span>
      </span>
    </div>

    <div class="contact">
      <h1 class="contact__name">MARCO T. DRUMMOND II</h1>
      <p class="contact__title">(Senior Project Manager)</p>
      <p class="contact__lines">
        (305) 555-0184<br>
        mdrummond.halcyongrandestates@mailbox.example
      </p>
    </div>

    <div class="company">
      <p class="company__name">HALCYON ARCHITECTURE LLC</p>
      <p class="company__address">4127 NW 52nd Ter. Suite 2308 Miami, FL 33148</p>
    </div>

    <div class="card__band"></div>
  </section>

</main>
</body>
</html>
```